Home page concept, possible logo colour change

There is no need to code a home page, we are just looking for concept ideas.
We have had a logo designed for a new company we are starting named Corvenhall Aluminium Windows & Doors. We are manufacturing bullet resistant window frames. We have had logo designed, we like the concept of the design, but the current colours (black and red) may not be the best option, especially when designing the website home page, and how it interacts with the logo colours. I have also attached the first draft of the home page which we are not happy with. The overall design/navigation is good, we have issues with the darkened out primary image and also the amount of red on the page, it just doesn't feel right. As mentioned before we are happy to look at colour changes to the logo.
Number of Pages Required
1 page
Look and feel
Each slider illustrates characteristics of the customer's brand and the style your logo design should communicate.

```html
<!DOCTYPE html>
<html lang="en">
<head>
<meta charset="utf-8">
<title>Corvenhall Aluminium Windows &amp; Doors</title>
<link href="https://fonts.googleapis.com/css2?family=Montserrat:wght@800&family=Poppins:wght@400;500;600&display=swap" rel="stylesheet">
<style>
:root{
  --navy:#06142b;
  --blue:#0a72c1;
  --blue-bright:#1b86d6;
  --ink:#1a1a1a;
  --text:#333;
  --muted:#555;
  --line:#d7e6f4;
  --white:#fff;
  --footer:#0b0b0c;
}
*{box-sizing:border-box;margin:0;padding:0}
html,body{width:1200px;height:3008px;overflow:hidden;background:var(--white)}
body{position:relative;font-family:"Poppins",sans-serif;color:var(--text)}
.abs{position:absolute}
.btn{position:absolute;display:flex;align-items:center;justify-content:center;gap:10px;background:var(--navy);color:var(--white);border-radius:7px;font-weight:500;text-decoration:none}
.btn .dot{width:16px;height:16px;border-radius:50%;background:var(--blue-bright);display:inline-flex;align-items:center;justify-content:center}
.btn-sm{font-size:10px;border-radius:5px;gap:6px}
.btn-sm .dot{width:11px;height:11px}

/* header */
.topline{left:0;top:0;width:1200px;height:3px;background:var(--blue)}
.header{left:0;top:3px;width:1200px;height:77px;background:var(--white)}
.brand{left:109px;top:20px;font-weight:600;font-size:25px;color:var(--ink);line-height:1}
.brand small{display:block;font-size:7.5px;font-weight:600;letter-spacing:.6px;margin-top:4px}
.nav{top:33px;font-size:15px;font-weight:500;color:#333}
.nav.active{color:var(--blue)}

/* hero */
.hero{left:0;top:80px;width:1200px;height:723px;background:linear-gradient(180deg,#5c6f86 0%,#a9c1da 30%,#c9dced 55%,#8ea7c0 62%,#cfdeed 80%,#a8bdd2 100%)}
.hero-frame{left:216px;top:194px;width:768px;height:348px;border:7px solid var(--blue-bright);background:rgba(255,255,255,.72)}
.hero-title{left:0;top:228px;width:1200px;text-align:center;font-family:"Montserrat",sans-serif;font-weight:800;font-size:52px;line-height:61px;color:var(--navy)}
.hero-sub{left:0;top:358px;width:1200px;text-align:center;font-size:22px;font-weight:600;color:var(--navy)}
.hero-copy{left:250px;top:394px;width:700px;text-align:center;font-size:14.5px;line-height:25px;color:#222}
.arrow{top:416px}

/* features */
.features{left:110px;top:652px;width:978px;height:292px;background:var(--white);border-radius:14px;box-shadow:0 8px 22px rgba(0,0,0,.1)}
.feature{position:absolute;top:0;width:326px;height:292px;text-align:center}
.feature + .feature{border-left:1px solid var(--line)}
.feature .ic{position:absolute;left:113px;top:36px}
.feature h3{position:absolute;top:136px;left:0;width:100%;font-size:20px;font-weight:500;color:var(--ink)}
.feature p{position:absolute;top:168px;left:20px;width:286px;font-size:12.5px;line-height:22px;color:#444}

/* products */
.section-title{left:0;top:1018px;width:1200px;text-align:center;font-family:"Montserrat",sans-serif;font-weight:800;font-size:37px;color:var(--ink)}
.title-rule{left:493px;top:1072px;width:212px;height:4px;background:var(--blue)}
.product{position:absolute;top:1110px;width:311px;height:450px;background:var(--white);border-radius:10px;box-shadow:0 6px 18px rgba(0,0,0,.12);overflow:hidden;text-align:center}
.product .photo{height:264px}
.product h4{margin-top:16px;font-size:23px;font-weight:500;color:var(--blue)}
.product p{margin:6px auto 0;width:280px;font-size:12.5px;line-height:21px;color:#444}
.product .btn{left:103px;top:391px;width:104px;height:31px}

/* blue panel */
.panel{left:111px;top:1646px;width:977px;height:435px;background:var(--blue);border-radius:14px}
.tile{position:absolute;top:1709px;width:248px;height:238px;background:var(--white);border-radius:8px;text-align:center}
.tile .ic{position:absolute;left:74px;top:40px}
.tile h4{position:absolute;left:0;top:170px;width:100%;font-size:20.5px;font-weight:600;color:#222}

/* accordion */
.frame-photo{left:182px;top:2195px;width:302px;height:330px;background:linear-gradient(135deg,#f2f2f2,#dadada 60%,#c4c4c4)}
.acc{position:absolute;left:531px;width:557px;border:1.5px solid #333;border-radius:6px;background:var(--white)}
.acc .label{position:absolute;left:29px;top:13px;font-size:17px;color:#222}
.acc .toggle{position:absolute;right:13px;top:17px}
.acc.open{border:2px solid var(--blue-bright)}
.acc-body{position:absolute;left:28px;top:50px;width:516px}
.acc-body p{font-size:11px;line-height:17.5px;letter-spacing:-.15px;color:#444;text-align:justify}
.acc-body .btn{position:static;display:inline-flex;margin-top:9px;width:125px;height:31px}

/* footer */
.footer{left:0;top:2608px;width:1200px;height:400px;background:var(--footer)}
.foot-brand{left:111px;top:2762px;font-size:30px;font-weight:600;color:var(--white);line-height:1}
.foot-brand small{display:block;font-size:8px;letter-spacing:.7px;margin-top:4px}
.foot-head{top:2660px;font-size:17px;font-weight:600;color:var(--white)}
.foot-rule{top:2696px;width:50px;height:2px;background:var(--blue)}
.foot-link{left:399px;font-size:13px;color:var(--white);letter-spacing:.3px}
.ci{position:absolute;left:636px;width:36px;height:36px;border-radius:50%;background:#2c2f35;display:flex;align-items:center;justify-content:center}
.ct{position:absolute;left:689px;font-size:13.5px;color:var(--white);line-height:19px}
.ct span{display:block;font-size:12.5px;color:#aaa}
.badge{left:1000px;top:2770px;width:64px;height:60px;background:#2f8f3e;border-radius:6px}
.foot-line{left:111px;top:2922px;width:977px;height:1px;background:#1d4f86}
.copy{left:0;top:2949px;width:1200px;text-align:center;font-size:14px;color:#ddd}
</style>
</head>
<body>

<div class="abs topline"></div>
<header class="abs header"></header>
<div class="abs brand">Corvenhall<small>ALUMINIUM WINDOWS &amp; DOORS</small></div>
<svg class="abs" style="left:528px;top:11px" width="16" height="16" viewBox="0 0 16 16"><path d="M8 0v16M0 8h16M2.5 2.5l11 11M13.5 2.5l-11 11" stroke="#0a72c1" stroke-width="1.6"/></svg>
<div class="abs nav active" style="left:513px">Home</div>
<div class="abs nav" style="left:596px">Our Products</div>
<div class="abs nav" style="left:732px">Why Corvenhall</div>
<a class="btn" style="left:901px;top:19px;width:187px;height:47px;font-size:16px">Make an Enquiry <span class="dot"><svg width="8" height="8" viewBox="0 0 8 8"><path d="M3 1.5 5.5 4 3 6.5" stroke="#fff" stroke-width="1.3" fill="none"/></svg></span></a>

<div class="abs hero" role="img" aria-label="Bright office interior with tall glazed windows and a reflective floor"></div>
<svg class="abs arrow" style="left:44px" width="24" height="50" viewBox="0 0 24 50"><path d="M22 2 2 25l20 23" stroke="#222" stroke-width="2" fill="none"/></svg>
<svg class="abs arrow" style="left:1132px" width="24" height="50" viewBox="0 0 24 50"><path d="M2 2l20 23L2 48" stroke="#222" stroke-width="2" fill="none"/></svg>
<div class="abs hero-frame"></div>
<h1 class="abs hero-title">BULLET RESISTANT<br>WINDOW &amp; DOORS</h1>
<div class="abs hero-sub">Your First Line Of Defence</div>
<p class="abs hero-copy">Dseste natus error sit voluptatem accusan tium doloremque laudantium, totam rem aperiam, ease aque ipaefdsa quae ab illo inventore veritatis ease quasi architecto.</p>
<a class="btn" style="left:525px;top:468px;width:150px;height:47px;font-size:16px">Get Started <span class="dot"><svg width="8" height="8" viewBox="0 0 8 8"><path d="M3 1.5 5.5 4 3 6.5" stroke="#fff" stroke-width="1.3" fill="none"/></svg></span></a>

<section class="abs features">
  <div class="feature" style="left:0">
    <svg class="ic" width="80" height="80" viewBox="0 0 80 80"><path d="M40 6 68 16v22c0 18-12 30-28 36C24 68 12 56 12 38V16z" fill="none" stroke="#111" stroke-width="2.5"/><path d="M40 14 60 21v17c0 13-8 22-20 27-12-5-20-14-20-27V21z" fill="none" stroke="#1b86d6" stroke-width="2.5"/><path d="m29 39 8 8 16-17" stroke="#1b86d6" stroke-width="4" fill="none"/></svg>
    <h3>Premium Protection</h3>
    <p>Werspiciatis asesertu undeas eomnis iste natus error asese sitvolasuptate masease accusantium emiumtotam.</p>
  </div>
  <div class="feature" style="left:326px">
    <svg class="ic" width="80" height="80" viewBox="0 0 80 80"><rect x="18" y="14" width="44" height="56" fill="none" stroke="#111" stroke-width="2.5"/><path d="m28 30 10-10M44 32l10-10M28 62l10-10M44 60l8-8" stroke="#1b86d6" stroke-width="2.5"/><path d="M20 8v8M16 12h8M64 54v8M60 58h8M10 38v8M6 42h8" stroke="#111" stroke-width="2"/></svg>
    <h3>Aesthetically Designed</h3>
    <p>Werspiciatis asesertu undeas eomnis iste natus error asese sitvolasuptate masease accusantium emiumtotam.</p>
  </div>
  <div class="feature" style="left:652px">
    <svg class="ic" width="90" height="80" viewBox="0 0 90 80"><rect x="12" y="16" width="46" height="38" fill="none" stroke="#111" stroke-width="2.5"/><path d="M58 28h14l10 12v14H58z" fill="none" stroke="#111" stroke-width="2.5"/><circle cx="26" cy="58" r="6" fill="#fff" stroke="#111" stroke-width="2.5"/><circle cx="70" cy="58" r="6" fill="#fff" stroke="#111" stroke-width="2.5"/><circle cx="38" cy="34" r="10" fill="none" stroke="#1b86d6" stroke-width="2.5"/><path d="M38 28v6h5M4 34h12M6 42h10" stroke="#1b86d6" stroke-width="2.5" fill="none"/></svg>
    <h3>Promptly Delivered</h3>
    <p>Werspiciatis asesertu undeas eomnis iste natus error asese sitvolasuptate masease accusantium emiumtotam.</p>
  </div>
</section>

<h2 class="abs section-title">SUPERIOR PROTECTION, SLEEK DESIGN</h2>
<div class="abs title-rule"></div>

<article class="product" style="left:110px">
  <div class="photo" role="img" aria-label="Silver aluminium framed glass door" style="background:linear-gradient(180deg,#f4f5f8,#e2e5ec)"></div>
  <h4>Dkseomas Mdalisek</h4>
  <p>Saerspiciatis unde omnis iste natus error sit voluptatem accusan tium doloremque laudantium otamrem.</p>
  <a class="btn btn-sm">Learn More <span class="dot"><svg width="6" height="6" viewBox="0 0 8 8"><path d="M3 1.5 5.5 4 3 6.5" stroke="#fff" stroke-width="1.5" fill="none"/></svg></span></a>
</article>
<article class="product" style="left:444px">
  <div class="photo" role="img" aria-label="Black aluminium framed glass door standing ajar" style="background:linear-gradient(180deg,#f6f6f7,#e4e5e8)"></div>
  <h4>Dkseomas Mdalisek</h4>
  <p>Saerspiciatis unde omnis iste natus error sit voluptatem accusan tium doloremque laudantium otamrem.</p>
  <a class="btn btn-sm">Learn More <span class="dot"><svg width="6" height="6" viewBox="0 0 8 8"><path d="M3 1.5 5.5 4 3 6.5" stroke="#fff" stroke-width="1.5" fill="none"/></svg></span></a>
</article>
<article class="product" style="left:778px">
  <div class="photo" role="img" aria-label="Dark building facade with reflective glazing and sky" style="background:linear-gradient(120deg,#3b4f6e 0%,#46618a 40%,#9cb9dc 60%,#d8e6f4 100%)"></div>
  <h4>Dkseomas Mdalisek</h4>
  <p>Saerspiciatis unde omnis iste natus error sit voluptatem accusan tium doloremque laudantium otamrem.</p>
  <a class="btn btn-sm">Learn More <span class="dot"><svg width="6" height="6" viewBox="0 0 8 8"><path d="M3 1.5 5.5 4 3 6.5" stroke="#fff" stroke-width="1.5" fill="none"/></svg></span></a>
</article>

<section class="abs panel"></section>
<div class="tile" style="left:172px">
  <svg class="ic" width="100" height="100" viewBox="0 0 100 100"><path d="M50 14 80 24v22c0 20-13 32-30 38C33 78 20 66 20 46V24z" fill="none" stroke="#111" stroke-width="3"/><path d="M50 22 72 30v16c0 14-9 24-22 29-13-5-22-15-22-29V30z" fill="none" stroke="#1b86d6" stroke-width="3"/><path d="m38 47 9 9 17-18" stroke="#1b86d6" stroke-width="4" fill="none"/><path d="M16 8v8M12 12h8M88 16v6M85 19h6" stroke="#1b86d6" stroke-width="2"/><path d="M14 74v2M14 80v2M14 86v2" stroke="#111" stroke-width="2"/></svg>
  <h4>Premium Protection</h4>
</div>
<div class="tile" style="left:472px">
  <svg class="ic" width="100" height="100" viewBox="0 0 100 100"><rect x="14" y="16" width="64" height="78" fill="none" stroke="#111" stroke-width="3.5"/><path d="M20 22h52v66H20zM46 22v66M20 55h52" fill="none" stroke="#111" stroke-width="2.5"/><path d="m26 38 10-10M52 76l10-10" stroke="#1b86d6" stroke-width="2.5"/><path d="M76 6v38M57 25h38M70 14l12 22M82 14 70 36" stroke="#1b86d6" stroke-width="2.5" fill="none"/></svg>
  <h4>Aesthetically Designed</h4>
</div>
<div class="tile" style="left:772px">
  <svg class="ic" width="100" height="100" viewBox="0 0 100 100"><path d="M14 28 46 14l32 14v38L46 82 14 66z" fill="none" stroke="#111" stroke-width="3"/><path d="M14 28l32 14 32-14M46 42v40M28 21l32 14v14" fill="none" stroke="#111" stroke-width="3"/><circle cx="74" cy="76" r="14" fill="#fff" stroke="#111" stroke-width="3"/><path d="m67 76 5 5 9-10" stroke="#1b86d6" stroke-width="3" fill="none"/></svg>
  <h4>Promptly Delivered</h4>
</div>
<a class="btn" style="left:505px;top:1974px;width:190px;height:46px;font-size:16px">Make an Enquiry <span class="dot"><svg width="8" height="8" viewBox="0 0 8 8"><path d="M3 1.5 5.5 4 3 6.5" stroke="#fff" stroke-width="1.3" fill="none"/></svg></span></a>

<div class="abs frame-photo" role="img" aria-label="Black aluminium window frame with frosted glass pane"></div>
<div class="acc" style="top:2170px;height:51px">
  <span class="label">Explore Our Range</span>
  <svg class="toggle" width="17" height="17" viewBox="0 0 17 17"><circle cx="8.5" cy="8.5" r="8.5" fill="#111"/><path d="M8.5 4.5v8M4.5 8.5h8" stroke="#fff" stroke-width="1.8"/></svg>
</div>
<div class="acc" style="top:2240px;height:51px">
  <span class="label">Make An Enquiry</span>
  <svg class="toggle" width="17" height="17" viewBox="0 0 17 17"><circle cx="8.5" cy="8.5" r="8.5" fill="#111"/><path d="M8.5 4.5v8M4.5 8.5h8" stroke="#fff" stroke-width="1.8"/></svg>
</div>
<div class="acc open" style="top:2310px;height:211px">
  <span class="label">Receive Customised Quote</span>
  <svg class="toggle" width="17" height="17" viewBox="0 0 17 17"><circle cx="8.5" cy="8.5" r="8.5" fill="#1b86d6"/><path d="M4.5 8.5h8" stroke="#fff" stroke-width="1.8"/></svg>
  <div class="acc-body">
    <p>Saerspiciatis undeasepoiise osamnis istasesee njhhjkatus error sit voluptatem accusan tium doloreasmque laudantium, totam rem aperiam, ease aque ipaefdsa quae ab illo inventore veritatis ease quasi architecto beatae vitae diascta sunt explicabo. Nemo enim ipsam voluptatem quia volupta sde sessitasese aspernatur autodit aut fugitsdsed quia conseq aauuntur magni dolores eos qui ratione voluptatem sequi nesciunt.</p>
    <a class="btn btn-sm">Make an Enquiry <span class="dot"><svg width="6" height="6" viewBox="0 0 8 8"><path d="M3 1.5 5.5 4 3 6.5" stroke="#fff" stroke-width="1.5" fill="none"/></svg></span></a>
  </div>
</div>

<footer class="abs footer"></footer>
<div class="abs foot-brand">Corvenhall<small>ALUMINIUM WINDOWS &amp; DOORS</small></div>

<div class="abs foot-head" style="left:397px">QUICK LINKS</div>
<div class="abs foot-rule" style="left:397px"></div>
<div class="abs foot-link" style="top:2718px">HOME</div>
<div class="abs foot-link" style="top:2744px">MAKE AN ENQUIRY</div>
<div class="abs foot-link" style="top:2770px">OUR PRODUCTS</div>
<div class="abs foot-link" style="top:2796px">BLOG</div>

<div class="abs foot-head" style="left:646px">CONTACT US</div>
<div class="abs foot-rule" style="left:646px"></div>
<div class="ci" style="top:2722px"><svg width="14" height="16" viewBox="0 0 14 16"><path d="M7 15s6-6 6-9.5A6 6 0 0 0 1 5.5C1 9 7 15 7 15z" fill="#1b86d6"/><circle cx="7" cy="5.5" r="2" fill="#2c2f35"/></svg></div>
<div class="ct" style="top:2718px"><span>Address</span>42 Harbour Lane Sydney,<br>NSW 2010 AU</div>
<div class="ci" style="top:2800px"><svg width="14" height="14" viewBox="0 0 14 14"><path d="M3 1h3l1 3-2 1.5a8 8 0 0 0 3.5 3.5L10 7l3 1v3c0 1-1 2-2 2A11 11 0 0 1 1 3c0-1 1-2 2-2z" fill="#1b86d6"/></svg></div>
<div class="ct" style="top:2795px"><span>Call Us</span>+61 (02) 5550 1427</div>
<div class="ci" style="top:2856px"><svg width="16" height="12" viewBox="0 0 16 12"><rect width="16" height="12" rx="1.5" fill="#1b86d6"/><path d="m1 1.5 7 5 7-5" stroke="#2c2f35" stroke-width="1.4" fill="none"/></svg></div>
<div class="ct" style="top:2851px"><span>Email</span>info@corvenhall.com</div>

<div class="abs foot-head" style="left:960px">QUALITY ASSURANCE</div>
<div class="abs foot-rule" style="left:960px"></div>
<div class="abs badge" role="img" aria-label="Quality certification badge"></div>

<div class="abs foot-line"></div>
<div class="abs copy">©2023. All rights reserved.</div>

</body>
</html>
```